Dravetti Business Cards

We need a business card design for Dravetti Mining.

This is a B2B company that buys and sells large machinery tires within the coal mining industry. The design should the strong, crisp and masculine. I have uploaded the company logo and rough mock-up of what the back of the card should look like. the front of the card should have the same look/feel as the back. I need editable templates for both the front and the back of the card.

Color scheme should be grey/green/black

Contact information to include on the card:
Name: Owen Pellsworth
Title: Managing Director
Phone: 972-555-0143
Address: 3157 Brantley #5 Dallas, TX 75209
Email: Owen@Dravetti-example.com

I am also opening a contest for letterhead design. If you submit a business card design, please also submit a letterhead design with the same look/feel. The winner of the business card design will also will the letter head and be paid for both.

Target Market(s)

Procurement men/women in the coal mining industry

Industry/Entity Type

Coal Mining

```html
<!DOCTYPE html>
<html lang="en">
<head>
<meta charset="utf-8">
<title>Dravetti Mining Business Cards</title>
<link rel="stylesheet" href="https://fonts.googleapis.com/css2?family=Ubuntu:wght@400;500;700&display=swap">
<style>
  :root {
    --backdrop: #e9e7e4;
    --card-light: #ffffff;
    --card-dark: #2a2a2a;
    --ink: #2b2b2b;
    --ink-soft: #3a3a3a;
    --logo-grey: #6b6b6b;
    --logo-light: #f2f2f2;
    --accent-green: #5fae37;
  }
  * { margin: 0; padding: 0; box-sizing: border-box; }
  html, body {
    width: 1200px;
    height: 900px;
    overflow: hidden;
  }
  body {
    background: var(--backdrop);
    font-family: "Ubuntu", sans-serif;
    position: relative;
  }
  .card {
    position: absolute;
    left: 354px;
    width: 488px;
    height: 278px;
    overflow: hidden;
    box-shadow: 0 2px 6px rgba(0, 0, 0, 0.18);
  }
  .card--front { top: 161px; background: var(--card-light); }
  .card--back { top: 471px; background: var(--card-dark); }

  .brand {
    position: absolute;
    left: 0;
    right: 0;
    display: flex;
    justify-content: center;
    align-items: center;
    gap: 10px;
  }
  .card--front .brand { top: 54px; }
  .card--back .brand { top: 122px; }
  .brand__mark {
    width: 30px;
    height: 30px;
    background: var(--accent-green);
  }
  .brand__name {
    font-weight: 700;
    font-size: 26px;
    line-height: 1;
    letter-spacing: 1px;
    text-transform: uppercase;
    white-space: nowrap;
  }
  .card--front .brand__name { color: var(--logo-grey); }
  .card--back .brand__name { color: var(--logo-light); }

  .holder {
    position: absolute;
    top: 200px;
    left: 0;
    right: 0;
    text-align: center;
    color: var(--ink);
    white-space: nowrap;
  }
  .holder__name { font-weight: 700; font-size: 15px; }
  .holder__title {
    font-size: 12px;
    text-transform: uppercase;
    margin-left: 3px;
  }
  .contact {
    position: absolute;
    top: 235px;
    left: 0;
    right: 0;
    text-align: center;
    font-size: 12.5px;
    color: var(--ink-soft);
    white-space: nowrap;
  }
  .contact__sep {
    color: var(--accent-green);
    margin: 0 3px;
  }

  .web-rule {
    position: absolute;
    top: 237px;
    left: 0;
    right: 0;
    display: flex;
    align-items: center;
    gap: 18px;
  }
  .web-rule__line {
    flex: 1;
    height: 1.5px;
    background: var(--accent-green);
  }
  .web-rule__url {
    flex: none;
    color: var(--logo-light);
    font-size: 13px;
    line-height: 18px;
    letter-spacing: 0.6px;
    white-space: nowrap;
  }
</style>
</head>
<body>
  <section class="card card--front" aria-label="Business card front">
    <div class="brand">
      <span class="brand__mark"></span>
      <span class="brand__name">Dravetti Mining</span>
    </div>
    <p class="holder">
      <span class="holder__name">Owen Pellsworth</span>
      <span class="holder__title">Managing Director</span>
    </p>
    <p class="contact">
      972-555-0143<span class="contact__sep">|</span>Owen@Dravetti-example.com<span class="contact__sep">|</span>3157 Brantley #5 Dallas, TX 75209
    </p>
  </section>

  <section class="card card--back" aria-label="Business card back">
    <div class="brand">
      <span class="brand__mark"></span>
      <span class="brand__name">Dravetti Mining</span>
    </div>
    <div class="web-rule">
      <span class="web-rule__line"></span>
      <span class="web-rule__url">www.Dravetti-example.com</span>
      <span class="web-rule__line"></span>
    </div>
  </section>
</body>
</html>
```